For Brivo: Business cards, letterhead, envelopes and double sided page

For Brivo: Previously described in email.

Business cards, letterhead, envelopes, and glossy marketing double sided page.

Marketing

```html
<!DOCTYPE html>
<html lang="en">
<head>
<meta charset="utf-8">
<title>Corvantis – Marketing Page</title>
<link href="https://fonts.googleapis.com/css2?family=Cormorant+Garamond:wght@500;600&family=Poiret+One&display=swap" rel="stylesheet">
<style>
  :root{
    --bg:#e9e6e1;
    --ink:#0c0c0c;
    --gold:#e6b567;
    --gold-deep:#c9954a;
    --stripe:#3a3a3c;
    --stripe-light:#55565a;
    --text-dark:#2a2118;
  }
  html,body{margin:0;height:100%;overflow:hidden;}
  body{width:1200px;height:1000px;background:var(--bg);display:flex;align-items:center;justify-content:center;}
  .page{position:relative;width:620px;height:900px;background:linear-gradient(160deg,#161616 0%,var(--ink) 55%);overflow:hidden;
    font-family:"Cormorant Garamond",Georgia,serif;font-weight:500;color:var(--gold);box-shadow:0 6px 24px rgba(0,0,0,.25);}
  .stripes{position:absolute;right:0;bottom:90px;width:360px;height:430px;}
  .content{position:relative;padding:22px 32px 0;}
  .brand{text-align:center;font-size:32px;font-weight:600;letter-spacing:6px;margin:0 0 8px;line-height:1;}
  p{margin:0 0 6px;font-size:12.4px;line-height:1.3;}
  .intro{text-align:justify;}
  .tab{display:inline-block;background:linear-gradient(90deg,var(--gold),var(--gold-deep));color:var(--ink);font-size:10px;letter-spacing:2.5px;font-weight:600;
    padding:3px 30px 3px 14px;margin:4px 0 6px -32px;clip-path:polygon(0 0,100% 0,calc(100% - 12px) 100%,0 100%);text-transform:uppercase;}
  ul{list-style:none;margin:0 0 6px;padding:0;font-size:12.4px;line-height:1.34;}
  li::before{content:"";display:inline-block;width:5px;height:5px;background:var(--gold);margin:0 7px 2px 0;}
  .row{display:flex;gap:16px;}
  .row > *{flex:1;}
  .collage{display:grid;grid-template-columns:1fr 1fr;gap:3px;height:108px;width:220px;flex:none;}
  .ph-a{background:linear-gradient(135deg,#1a2a4a,#0d1320 70%,#2b4a7a);}
  .ph-b{background:linear-gradient(135deg,#4a4a44,#22221f);}
  .ph-c{background:linear-gradient(135deg,#1d3a5a,#0b1422 60%,#7fb0d9);}
  .ph-d{background:linear-gradient(135deg,#8a6a4a,#3a2a1c);}
  .gallery{display:flex;gap:4px;height:104px;margin:4px -32px 4px;}
  .g1{flex:1.25;background:linear-gradient(160deg,#2a3f8a,#6d7ec4 40%,#0e1330);}
  .g2{flex:1;background:linear-gradient(170deg,#1f4a4a,#4f8a86 45%,#16231f);}
  .g3{flex:1;background:linear-gradient(160deg,#9fa4aa,#4a4e54 60%,#2a2c30);}
  .footer{position:absolute;left:0;bottom:0;width:100%;height:110px;}
  .footer-wave{position:absolute;inset:0;width:100%;height:100%;}
  .contact{position:absolute;left:0;right:0;bottom:14px;display:flex;justify-content:space-between;align-items:flex-end;padding:0 30px;
    font-family:"Poiret One",Arial,sans-serif;color:var(--text-dark);font-size:14px;line-height:1.2;}
  .contact .item{display:flex;gap:8px;align-items:flex-start;}
  .icon{flex:none;}
</style>
</head>
<body>
<article class="page">
  <svg class="stripes" viewBox="0 0 360 430" aria-hidden="true">
    <polygon points="360,0 360,40 40,430 0,430" fill="var(--stripe)"/>
    <polygon points="360,80 360,120 110,430 70,430" fill="var(--stripe-light)"/>
    <polygon points="360,150 360,200 190,430 140,430" fill="var(--stripe)"/>
    <polygon points="360,240 360,270 250,430 220,430" fill="var(--stripe-light)"/>
    <polygon points="360,310 360,350 320,430 280,430" fill="var(--stripe)"/>
  </svg>

  <div class="content">
    <h1 class="brand">CORVANTIS</h1>
    <p class="intro">Corvantis Inc. is a recognized leader in the Cinema and Broadcast post production, Distribution, and Exhibition fields. Based in New York City, our company provides experienced engineers for all aspects of presentation technologies, throughout the United States and abroad. Hollywood Film Studios, Commercial Movie Theatres, Cultural Centers, Universities and private executive screening venues utilize Corvantis' wide range of technological expertise. Although specializing in Digital Cinema and motion picture film formats, our company also provides service and support for non cinema audio visual applications.</p>

    <div class="tab">Premieres / Screenings</div>
    <p>Corvantis represents all interests of the Hollywood film community for technical representation at screenings and events.</p>
    <div class="row">
      <ul>
        <li>Guild, Critic, All Media, &amp; Promotional Screenings</li>
        <li>Recruited Research Preview Screenings</li>
        <li>Production Dailies</li>
        <li>Opening Weekend Tech Checks</li>
        <li>"Upfront" Network Presentations</li>
        <li>Motion Picture Premieres and Tastemaker Red Carpet Events</li>
      </ul>
      <div class="collage">
        <div class="ph-a" role="img" aria-label="Photo of a screening room with a lit screen"></div>
        <div class="ph-b" role="img" aria-label="Photo of a projection booth"></div>
        <div class="ph-c" role="img" aria-label="Photo of a theatre auditorium"></div>
        <div class="ph-d" role="img" aria-label="Photo of a lounge screening venue"></div>
      </div>
    </div>
    <p>Corvantis supplies equipment and engineering services for screening events in non-cinema venues. Our inventory of rental equipment includes:</p>
    <div class="row">
      <ul>
        <li>Orvanta 4K Digital Cinema Projectors</li>
        <li>Tessavox Digital Servers and Audio Processors</li>
        <li>Tessavox / Quillo 3D Systems</li>
        <li>Halvane Sound Systems</li>
      </ul>
      <ul style="padding-top:17px">
        <li>Traditional matte white perforated screens</li>
        <li>3d silver screens (Quillo 3D)</li>
        <li>Legacy film equipment (35mm 70mm 16mm)</li>
      </ul>
    </div>

    <div class="tab">Cinema Installation / Multiplex Service</div>
    <p>Corvantis provides equipment sales, installation and contractual maintenance services for all presentation facilities. Commercial theatre chains, Independent Theatre Owners, Universities, Museums, and Industry / Executive Screening Rooms are examples of our wide range of clients.</p>
    <div class="gallery">
      <div class="g1" role="img" aria-label="Photo of a cinema screen with colourful projection"></div>
      <div class="g2" role="img" aria-label="Photo of a multiplex auditorium with seating"></div>
      <div class="g3" role="img" aria-label="Photo of projection and control equipment"></div>
    </div>

    <div class="tab">Service We Offer</div>
    <div class="row">
      <ul style="flex:1.5">
        <li>Consulting services to architects / contractors / ownership</li>
        <li>Network operations center (noc) / remote site monitoring</li>
        <li>In field emergency service and scheduled routine maintenance</li>
      </ul>
      <ul style="padding-top:17px">
        <li>Installation, integration, training</li>
        <li>Equipment sales</li>
      </ul>
    </div>
  </div>

  <footer class="footer">
    <svg class="footer-wave" viewBox="0 0 620 110" preserveAspectRatio="none" aria-hidden="true">
      <path d="M0,22 L0,110 L620,110 L620,0 C480,46 300,38 0,22 Z" fill="var(--gold)"/>
    </svg>
    <div class="contact">
      <div class="item">
        <svg class="icon" width="14" height="20" viewBox="0 0 14 20" aria-hidden="true"><path d="M7 0a7 7 0 0 0-7 7c0 5 7 13 7 13s7-8 7-13a7 7 0 0 0-7-7zm0 10a3 3 0 1 1 0-6 3 3 0 0 1 0 6z" fill="var(--text-dark)"/></svg>
        <div>410 W. 52nd St.<br>New York, N.Y. 10019<br>Suite 12</div>
      </div>
      <div class="item">
        <svg class="icon" width="18" height="18" viewBox="0 0 24 24" aria-hidden="true"><path d="M6.6 10.8a15 15 0 0 0 6.6 6.6l2.2-2.2c.3-.3.7-.4 1-.2 1.1.4 2.3.6 3.6.6.6 0 1 .4 1 1V20c0 .6-.4 1-1 1A17 17 0 0 1 3 4c0-.6.4-1 1-1h3.5c.6 0 1 .4 1 1 0 1.3.2 2.5.6 3.6.1.3 0 .7-.2 1z" fill="var(--text-dark)"/></svg>
        <div>T: 212-555-0140<br>F: 212-555-0141</div>
      </div>
      <div class="item" style="align-items:center">
        <svg class="icon" width="22" height="16" viewBox="0 0 22 16" aria-hidden="true"><rect x="1" y="1" width="20" height="14" fill="none" stroke="var(--text-dark)" stroke-width="1.6"/><path d="M1 1l10 8 10-8" fill="none" stroke="var(--text-dark)" stroke-width="1.6"/></svg>
        <div>info@corvantismedia.com</div>
      </div>
    </div>
  </footer>
</article>
</body>
</html>
```